Security based company delivering High Risk Training to Law Enforcement Agencies Worldwide.

We need a Web design for a company doing business in Washington D.C. We deliver High Risk Training to Law Enforcement Agencies throughout the world. Our focus is on Improvised Explosive Devices. We train Bomb Technicians and First Responders in all aspects relating to bombings and criminal incidents globally.

Reason: We have uploaded our logo. Thank you.

Target Market(s)

Military and Law Enforcement Personnel from around the world.

Industry/Entity Type

Business

Requirements
Should not have
• Do not include cartoon like characters.

```html
<!DOCTYPE html>
<html lang="en">
<head>
<meta charset="utf-8">
<title>Vantrel International — High Risk Training</title>
<link rel="stylesheet" href="https://fonts.googleapis.com/css2?family=Open+Sans:wght@400;600;700&display=swap">
<style>
  :root {
    --header-bg: #2e2e2e;
    --header-edge: #1f1f1f;
    --nav-olive: #8b9573;
    --nav-olive-dark: #6f7a58;
    --nav-active: #a9b38f;
    --text-light: #ffffff;
    --text-muted: #b9b9b9;
    --dropdown-blue: #3a98d0;
    --caption-dark: rgba(60, 60, 60, 0.88);
    --caption-tan: rgba(150, 112, 78, 0.9);
    --band-blue: #3b97cf;
    --arrow-bg: rgba(70, 70, 70, 0.85);
  }
  * { box-sizing: border-box; margin: 0; padding: 0; }
  html, body {
    width: 1200px; height: 733px; overflow: hidden;
    background: var(--header-bg);
    font-family: "Open Sans", Arial, sans-serif;
  }
  .site { position: relative; width: 1200px; height: 733px; }

  .site-header {
    height: 145px; background: var(--header-bg);
    border-bottom: 3px solid var(--header-edge);
    position: relative;
  }
  .brand {
    position: absolute; left: 92px; top: 36px;
    display: flex; align-items: center; gap: 16px;
  }
  .brand-mark {
    width: 70px; height: 70px; border-radius: 50%;
    background: #5a5a5a;
  }
  .brand-name {
    color: var(--text-light); font-weight: 700; font-size: 40px;
    line-height: 1; letter-spacing: 1px;
  }
  .brand-name small { display: block; font-size: 18px; letter-spacing: 3px; margin-top: 6px; }

  .contact {
    position: absolute; right: 100px; top: 20px;
    display: flex; gap: 22px; color: var(--text-muted); font-size: 17px;
    align-items: center;
  }
  .contact span { display: flex; align-items: center; gap: 8px; }
  .social {
    position: absolute; right: 100px; top: 58px; display: flex; gap: 10px;
  }
  .social i {
    display: block; width: 30px; height: 30px;
    background: #4a4a4a; border: 1px solid #6a6a6a;
  }
  .tagline {
    position: absolute; right: 100px; top: 104px;
    color: var(--text-light); font-weight: 600; font-size: 17px;
  }

  .main-nav {
    height: 40px; background: var(--nav-olive);
    border-bottom: 2px solid var(--nav-olive-dark);
    display: flex; padding-left: 95px; position: relative;
  }
  .main-nav a {
    color: #2a2a2a; text-decoration: none; font-size: 14px;
    padding: 0 16px; line-height: 40px; font-family: Arial, sans-serif;
  }
  .main-nav a.current { color: var(--text-light); background: var(--nav-olive-dark); }
  .main-nav a.open { color: var(--text-light); background: var(--nav-active); }
  .dropdown {
    position: absolute; left: 283px; top: 40px; width: 178px; z-index: 3;
    font-family: Arial, sans-serif; font-size: 13px;
  }
  .dropdown li { list-style: none; height: 32px; line-height: 32px; padding-left: 22px; }
  .dropdown .active { background: var(--dropdown-blue); color: var(--text-light); }
  .dropdown .item { background: #fff; color: #333; padding-left: 10px; }

  .hero {
    position: relative; height: 490px;
    background: linear-gradient(180deg, #c7c9c4 0%, #d9cbb1 45%, #c8ad85 100%);
  }
  .caption-title, .caption-sub {
    position: absolute; left: 317px; width: 566px;
    color: var(--text-light); text-align: center;
  }
  .caption-title {
    top: 192px; height: 56px; line-height: 56px;
    background: var(--caption-dark); font-size: 32px; font-weight: 600;
  }
  .caption-sub {
    top: 265px; height: 48px; line-height: 48px;
    background: var(--caption-tan); font-size: 21px; font-weight: 600;
  }
  .slide-arrow {
    position: absolute; top: 180px; width: 54px; height: 54px;
    border-radius: 50%; background: var(--arrow-bg);
    display: flex; align-items: center; justify-content: center;
  }
  .slide-arrow.prev { left: 94px; }
  .slide-arrow.next { right: 94px; }
  .slide-dots {
    position: absolute; bottom: 10px; left: 575px; display: flex; gap: 4px;
  }
  .slide-dots i {
    width: 14px; height: 14px; border-radius: 50%;
    border: 2px solid #eee; display: block;
  }
  .slide-dots i.on { background: #eee; }

  .section-band {
    height: 58px; background: var(--band-blue);
    border-top: 3px solid #2c7fb2;
    display: flex; align-items: center; justify-content: center; gap: 12px;
    color: var(--text-light); font-size: 26px; font-weight: 600;
  }
  .section-band .dot { width: 22px; height: 22px; border-radius: 50%; background: #2b2b2b; }
</style>
</head>
<body>
<div class="site">
  <header class="site-header">
    <div class="brand">
      <div class="brand-mark"></div>
      <div class="brand-name">VANTREL<small>INTERNATIONAL</small></div>
    </div>
    <div class="contact">
      <span>
        <svg width="16" height="12" viewBox="0 0 16 12"><rect width="16" height="12" fill="#b9b9b9"/><path d="M0 0l8 7 8-7" stroke="#2e2e2e" stroke-width="1.5" fill="none"/></svg>
        info@vantrelintl.com
      </span>
      <span>
        <svg width="14" height="14" viewBox="0 0 14 14"><path d="M3 0l3 3-2 2c1 2 3 4 5 5l2-2 3 3-2 3C6 13 1 8 0 3z" fill="#b9b9b9"/></svg>
        0142867390
      </span>
    </div>
    <div class="social"><i></i><i></i><i></i><i></i></div>
    <p class="tagline">High Risk Training for Law Enforcement Agencies Worldwide</p>
  </header>

  <nav class="main-nav">
    <a class="current">HOME</a>
    <a>ABOUT US</a>
    <a class="open">SERVICES</a>
    <a>COURSES</a>
    <a>CONTACT US</a>
    <ul class="dropdown">
      <li class="active">TRAINING</li>
      <li class="item">›&nbsp; SERVICES</li>
    </ul>
  </nav>

  <section class="hero" role="img" aria-label="Photo of a bomb technician in a protective suit working beside a stop sign at a desert training site">
    <div class="slide-arrow prev">
      <svg width="18" height="22" viewBox="0 0 18 22"><path d="M14 2L4 11l10 9" stroke="#fff" stroke-width="4" fill="none"/></svg>
    </div>
    <div class="slide-arrow next">
      <svg width="18" height="22" viewBox="0 0 18 22"><path d="M4 2l10 9-10 9" stroke="#fff" stroke-width="4" fill="none"/></svg>
    </div>
    <h1 class="caption-title">COUNTER I.E.D. TRAINING</h1>
    <p class="caption-sub">High Level Courses in Identification and Disposal</p>
    <div class="slide-dots"><i></i><i class="on"></i><i></i></div>
  </section>

  <div class="section-band"><span class="dot"></span>WHO WE ARE</div>
</div>
</body>
</html>
```